Looking for Landingpage / Website Designer

We are looking for a Web Designer / Developer for our upcoming Start Up Websites. The first project will be a simple responsive business website with a CTA- Button and an optional Newsletter Opt-In. We do aim for a modern online business approach, since we are a young company.

It is necessary to understand, that we need a conversion orientated design, not a wordpress blog with widgets and galleries.

We are currently discussing how it is going to happen and what preferences we need to focus on.

What we know is, that it should be more of a landing page with an option of adding 2 or 3 Navigation points.

We even thought about using services like plumvesta.com or crintofold.com to have an easier approach for future customizations and A/B testing.

We'd love to see how you fit the design/colors to the upcoming logo
(which is not the final version yet )

hope you can do something about that.

For the Structure.

1. Bracket

Slogan plus a preview text of what we are offering. On the right side a video placeholder plus CTA button.

2. Bracket

Illustrating 3 Benefits. On the right side - Opt in for Contact/Newsletter and CTA Button

3. Bracket

Picture with text just like you have it with the testimonial

You can orientate yourself towards to that landing page example as well:

http://cdn2.zorvellink.net/hub/53/file-581676469-png/Blog-Related_Images/plumvesta_landing_page.png?t=1416543075530

If our collaboration is going well, we would like to stay in touch for further projects.
Updates

Reason: There are 3 Design we do really like but, don't fit exactly our needs. 5 Days max.

Reason: For final adjustments.

I just uploaded the final logo :) Thank you for your commitment so far!

Target Market(s)

Our targeted audience could be almost everybody, who looks for an average paid side job (students, unemployed, house wives and whatever you can imagine). Maybe this is enough information for you to get a mere perception of what this is all about.

Industry/Entity Type

Business

Coding

Coded - Design and coding required

Font styles to use
Serif
Sans Serif

Colors
acd037
5c5c5c
33a6d7

Requirements
Must have
• Registration Opt-In
Responsive on any Device
Customizable
A benefits navigation just like in that example I've uploaded.
Nice to have
• As fast as possible ;D

```html
<!DOCTYPE html>
<html lang="en">
<head>
<meta charset="utf-8">
<title>Corvanta.de – What We Offering</title>
<link href="https://fonts.googleapis.com/css2?family=Oswald:wght@400;500;600&family=Nunito+Sans:ital,wght@0,400;0,600;0,700;1,400;1,600&display=swap" rel="stylesheet">
<style>
  :root {
    --green: #acd037;
    --green-dark: #86b01c;
    --footer-green: #94b61d;
    --blue: #33a6d7;
    --grey: #5c5c5c;
    --header-bg: #2a2a2a;
    --hero-deep: #0a1422;
    --hero-mid: #1d3a52;
    --line: #e3e3e3;
    --panel: #f1f1f1;
  }
  * { box-sizing: border-box; margin: 0; padding: 0; }
  html, body { width: 1114px; height: 1200px; overflow: hidden; background: #fff; }
  body { position: relative; font-family: "Nunito Sans", sans-serif; color: var(--grey); }
  .abs { position: absolute; }

  /* Header */
  .site-header { left: 0; top: 0; width: 1114px; height: 82px; background: var(--header-bg); }
  .brand { left: 69px; top: 22px; display: flex; align-items: center; gap: 8px;
    font-family: "Nunito Sans", sans-serif; font-weight: 700; font-size: 32px; color: var(--green); }
  .brand-dot { width: 38px; height: 38px; border-radius: 50%; background: var(--green); }
  .connect { right: 68px; top: 27px; display: flex; align-items: center; gap: 5px; }
  .connect-label { font-size: 11px; font-style: italic; color: #ddd; margin-right: 6px; }
  .social-dot { width: 27px; height: 27px; border-radius: 50%; background: #9a9a9a; }

  /* Hero */
  .hero { left: 0; top: 82px; width: 1114px; height: 381px;
    background: radial-gradient(ellipse at 25% 85%, #3f6d88 0%, var(--hero-mid) 30%, var(--hero-deep) 70%); }
  .hero-title { left: 69px; top: 75px; font-family: "Oswald", sans-serif; font-weight: 600;
    font-size: 44px; line-height: 1.1; color: var(--blue); }
  .hero-text { left: 69px; top: 130px; width: 460px; font-size: 15.5px; line-height: 23px; color: #fff; }
  .btn { display: flex; align-items: center; justify-content: center; color: #fff;
    background: linear-gradient(#a6cc2e, var(--green-dark)); font-weight: 600; text-transform: uppercase;
    border-radius: 2px; }
  .hero-cta { left: 69px; top: 245px; width: 197px; height: 41px; font-size: 16px; letter-spacing: .3px; }
  .video { left: 571px; top: 46px; width: 475px; height: 278px; border: 3px solid #fff;
    background: linear-gradient(135deg, #55677a, #2f3c4a 55%, #445566); }
  .play { left: 50%; top: 50%; width: 74px; height: 52px; margin: -26px 0 0 -37px;
    border-radius: 12px; background: #d8302a; }

  /* Section headings */
  .section-title { font-family: "Oswald", sans-serif; font-weight: 400; color: var(--blue);
    font-size: 44px; line-height: 1; display: flex; align-items: center; gap: 16px; }
  .brace { font-family: "Oswald", sans-serif; font-weight: 400; font-size: 62px; color: #c8c8c8; line-height: 1; }

  /* Benefits */
  .benefits-title { left: 69px; top: 520px; }
  .benefit-track { left: 267px; top: 546px; width: 517px; height: 4px; background: var(--green-dark); }
  .benefit { width: 160px; text-align: center; }
  .hex { display: block; margin: 0 auto; }
  .benefit-heading { margin-top: 12px; font-size: 15px; font-weight: 600; color: var(--blue); }
  .benefit-text { margin-top: 6px; font-size: 11.5px; line-height: 17px; color: #555; }
  .divider { left: 69px; top: 708px; width: 726px; height: 1px; background: var(--line); }

  /* Testimonials */
  .testimonials-title { left: 69px; top: 742px; }
  .avatar { width: 75px; height: 75px; border: 1px solid var(--line); padding: 3px; background: #fff; }
  .avatar-fill { width: 100%; height: 100%; background: linear-gradient(#e8ecef, #b7bfc7); }
  .quote { width: 255px; height: 142px; border: 1px solid var(--line); background: #fff; padding: 16px 17px; }
  .quote::before { content: ""; position: absolute; left: -9px; top: 14px; width: 15px; height: 15px;
    background: #fff; border-left: 1px solid var(--line); border-bottom: 1px solid var(--line); transform: rotate(45deg); }
  .quote-text { font-size: 11.5px; font-style: italic; line-height: 17px; color: #555; }
  .quote-name { margin-top: 13px; font-size: 11.5px; font-style: italic; color: var(--blue); }
  .quote-role { font-size: 10px; color: var(--green-dark); }

  /* Quick contact */
  .contact-panel { left: 820px; top: 512px; width: 226px; height: 438px; background: var(--panel);
    border: 1px solid #dedede; box-shadow: inset 0 0 0 3px #fff; }
  .contact-title { left: 18px; top: 18px; font-family: "Oswald", sans-serif; font-weight: 500;
    font-size: 42px; line-height: 46px; color: var(--blue); }
  .field { left: 18px; width: 188px; height: 31px; background: #fff; border: 1px solid #e0e0e0;
    font-size: 11px; font-style: italic; color: #999; padding: 9px 12px; }
  .submit { left: 66px; top: 385px; width: 140px; height: 32px; font-size: 16px; }

  /* Footer */
  .site-footer { left: 0; top: 1140px; width: 1114px; height: 60px; background: var(--footer-green);
    display: flex; align-items: center; justify-content: center; font-size: 10.5px; color: #e6f0c4; }
</style>
</head>
<body>

<header class="site-header abs">
  <div class="brand abs"><span class="brand-dot"></span>Corvanta.de</div>
  <div class="connect abs">
    <span class="connect-label">Connect Us:</span>
    <span class="social-dot" aria-label="Social link"></span>
    <span class="social-dot" aria-label="Social link"></span>
    <span class="social-dot" aria-label="Social link"></span>
    <span class="social-dot" aria-label="Social link"></span>
    <span class="social-dot" aria-label="Social link"></span>
  </div>
</header>

<section class="hero abs" role="img" aria-label="Dark blue background with a wave of glowing dots">
  <h1 class="hero-title abs">What We Offering</h1>
  <p class="hero-text abs">Aliquam molestie, mi et imperdiet euismod, dui purus auctor tellus, et interdum lacus lectus et ante. Sed accumsan sollicitudin sapien, sit amet adipiscing turpis gravida ac egestas risus in magna varius commodo.</p>
  <a class="btn hero-cta abs">Let's Get Started</a>
  <div class="video abs" role="img" aria-label="Video placeholder: group of business people in suits">
    <div class="play abs">
      <svg width="74" height="52" viewBox="0 0 74 52"><polygon points="30,15 30,37 48,26" fill="#fff"/></svg>
    </div>
  </div>
</section>

<h2 class="section-title benefits-title abs">BENEFITS <span class="brace">{</span></h2>
<div class="benefit-track abs"></div>

<div class="benefit abs" style="left:258px;top:513px">
  <svg class="hex" width="62" height="70" viewBox="0 0 62 70"><polygon points="31,0 62,17.5 62,52.5 31,70 0,52.5 0,17.5" fill="var(--green-dark)"/><text x="31" y="50" text-anchor="middle" font-family="Oswald, sans-serif" font-size="40" fill="#fff">1</text></svg>
  <h3 class="benefit-heading">Benefit Heading</h3>
  <p class="benefit-text">Vestibulum ante ipsum primis in faucibus orci luctus et ultrices posuere..</p>
</div>
<div class="benefit abs" style="left:444px;top:513px">
  <svg class="hex" width="62" height="70" viewBox="0 0 62 70"><polygon points="31,0 62,17.5 62,52.5 31,70 0,52.5 0,17.5" fill="var(--green-dark)"/><text x="31" y="50" text-anchor="middle" font-family="Oswald, sans-serif" font-size="40" fill="#fff">2</text></svg>
  <h3 class="benefit-heading">Benefit Heading</h3>
  <p class="benefit-text">Vestibulum ante ipsum primis in faucibus orci luctus et ultrices posuere..</p>
</div>
<div class="benefit abs" style="left:629px;top:513px">
  <svg class="hex" width="62" height="70" viewBox="0 0 62 70"><polygon points="31,0 62,17.5 62,52.5 31,70 0,52.5 0,17.5" fill="var(--green-dark)"/><text x="31" y="50" text-anchor="middle" font-family="Oswald, sans-serif" font-size="40" fill="#fff">3</text></svg>
  <h3 class="benefit-heading">Benefit Heading</h3>
  <p class="benefit-text">Vestibulum ante ipsum primis in faucibus orci luctus et ultrices posuere..</p>
</div>

<div class="divider abs"></div>

<h2 class="section-title testimonials-title abs">TESTIMONIALS <span class="brace">{</span></h2>

<div class="avatar abs" style="left:68px;top:814px"><div class="avatar-fill" role="img" aria-label="Portrait photo of a smiling businesswoman"></div></div>
<div class="quote abs" style="left:165px;top:814px">
  <p class="quote-text">“Aliquam molestie, mi et imperdiet euismod, dui purus auctor tellus, et interdum lacus lectus et ante. Sed accumsan sollicitudin sapien, sit amet adipiscing turpis gravida ac...”</p>
  <p class="quote-name">Lena Morrow <span class="quote-role">(Manager)</span></p>
</div>
<div class="avatar abs" style="left:443px;top:814px"><div class="avatar-fill" role="img" aria-label="Portrait photo of a businessman in a suit"></div></div>
<div class="quote abs" style="left:541px;top:814px">
  <p class="quote-text">“Aliquam molestie, mi et imperdiet euismod, dui purus auctor tellus, et interdum lacus lectus et ante. Sed accumsan sollicitudin sapien, sit amet adipiscing turpis gravida ac...”</p>
  <p class="quote-name">Lena Morrow <span class="quote-role">(Manager)</span></p>
</div>
<div class="avatar abs" style="left:68px;top:977px"><div class="avatar-fill" role="img" aria-label="Portrait photo of a smiling man with glasses"></div></div>
<div class="quote abs" style="left:165px;top:977px">
  <p class="quote-text">“Aliquam molestie, mi et imperdiet euismod, dui purus auctor tellus, et interdum lacus lectus et ante. Sed accumsan sollicitudin sapien, sit amet adipiscing turpis gravida ac...”</p>
  <p class="quote-name">Lena Morrow <span class="quote-role">(Manager)</span></p>
</div>
<div class="avatar abs" style="left:443px;top:977px"><div class="avatar-fill" role="img" aria-label="Portrait photo of a smiling young man"></div></div>
<div class="quote abs" style="left:541px;top:977px">
  <p class="quote-text">“Aliquam molestie, mi et imperdiet euismod, dui purus auctor tellus, et interdum lacus lectus et ante. Sed accumsan sollicitudin sapien, sit amet adipiscing turpis gravida ac...”</p>
  <p class="quote-name">Lena Morrow <span class="quote-role">(Manager)</span></p>
</div>

<aside class="contact-panel abs">
  <h2 class="contact-title abs">QUICK<br>CONTACT</h2>
  <div class="field abs" style="top:127px">Name</div>
  <div class="field abs" style="top:166px">Email Address</div>
  <div class="field abs" style="top:204px">Company</div>
  <div class="field abs" style="top:242px">Contact No.</div>
  <div class="field abs" style="top:281px;height:88px">Contact No.</div>
  <a class="btn submit abs">Submit Now</a>
</aside>

<footer class="site-footer abs">Copyright © 2014.Company Name. All Right Reserved</footer>

</body>
</html>
```